EV Charging Station Integrator needs a website for Brevok

We need a website to inform our customers and partners of what we do. At Brevok, we plan, design, and deploy EVcharging Solutions as a Service by leveraging a best-in-class multi-vendor and partner network with expertise to deliver EV Hardware, Software and Services as Turn-Key and Agnostic solutions.

The website should have 3 pages + contact (HOME, THE PROBLEM, THE SOLUTION) + Contact information. Please see PPT attached for suggested framework.

```html
<!DOCTYPE html>
<html lang="en">
<head>
<meta charset="utf-8">
<title>Brevok EV Charging</title>
<link href="https://fonts.googleapis.com/css2?family=Montserrat:wght@400;500;600;700;800&family=Mulish:wght@400;600;700&display=swap" rel="stylesheet">
<style>
:root{
  --orange:#f7941d;
  --orange-light:#fbb03b;
  --orange-deep:#f26b1d;
  --navy:#0d2a6b;
  --navy-deep:#082260;
  --ink:#222;
  --muted:#555;
  --panel:#f2f2f2;
  --white:#fff;
}
*{box-sizing:border-box;margin:0;padding:0}
html,body{width:1200px;height:3783px;overflow:hidden}
body{position:relative;background:var(--white);font-family:"Mulish",sans-serif;color:var(--ink)}
.section{position:absolute;left:0;width:1200px;overflow:hidden}
.heading{font-family:"Montserrat",sans-serif;font-weight:700;text-align:center;font-size:19px;letter-spacing:.3px;color:var(--ink)}
.heading-rule{display:block;width:28px;height:2px;background:var(--orange);margin:14px auto 0}

/* header + hero */
.hero{top:0;height:665px;background:#f7f7f7}
.hero-photo{position:absolute;inset:0 0 40px 0;
  background:
    radial-gradient(ellipse 120px 90px at 835px 215px,rgba(90,200,255,.9),rgba(40,140,255,0) 70%),
    radial-gradient(ellipse 260px 380px at 1010px 300px,#f4f6f9 0%,#c9d1dc 55%,rgba(150,165,185,0) 80%),
    radial-gradient(ellipse 120px 300px at 820px 360px,#1b1d22 0%,#33363d 50%,rgba(50,55,65,0) 80%),
    radial-gradient(ellipse 500px 200px at 250px 480px,rgba(120,210,255,.85),rgba(40,120,230,0) 70%),
    linear-gradient(100deg,#0b2f7a 0%,#1660c4 28%,#5a8fcf 48%,#b8c6d8 62%,#e7ecf2 80%,#9aa7b8 100%)}
.site-header{position:absolute;top:0;left:0;width:1200px;height:55px;background:rgba(24,48,112,.82);z-index:2}
.brand{position:absolute;left:132px;top:16px;font-family:"Montserrat",sans-serif;font-weight:700;font-size:19px;letter-spacing:5px;color:var(--white)}
.nav{position:absolute;right:92px;top:13px;display:flex;gap:10px}
.nav a{font-family:"Montserrat",sans-serif;font-weight:600;font-size:12px;color:var(--white);text-decoration:none;padding:7px 12px}
.nav a.active{background:var(--orange)}
.hero-box{position:absolute;left:132px;top:219px;width:325px;height:241px;background:rgba(28,52,120,.82);padding:26px 32px}
.hero-box h1{font-family:"Montserrat",sans-serif;font-weight:800;font-size:25.5px;line-height:34px;letter-spacing:-.2px;color:var(--white)}
.btn-read{display:inline-block;margin-top:20px;background:var(--orange);color:var(--white);font-family:"Montserrat",sans-serif;font-weight:800;font-size:11px;padding:9px 12px;border:2px solid var(--orange-light)}
.dots{position:absolute;top:609px;left:562px;display:flex;gap:10px}
.dots span{width:8px;height:8px;background:var(--white)}
.dots span.on{background:var(--orange)}
.hero-curve{position:absolute;left:0;bottom:0}

/* why */
.why{top:665px;height:662px;background:linear-gradient(135deg,#f8f8f8 0%,#ececec 45%,#f7f7f7 55%,#e9e9e9 100%)}
.why .heading{margin-top:78px}
.cards{position:absolute;top:149px;left:131px;display:flex;gap:26px}
.card{position:relative;width:295px;height:470px}
.card-shape{position:absolute;inset:0}
.card-body{position:relative;padding:44px 38px 0;text-align:center}
.card-icon{display:block;margin:0 auto}
.card h3{font-family:"Montserrat",sans-serif;font-weight:700;font-size:12.5px;line-height:19px;margin-top:20px;color:var(--ink)}
.card .heading-rule{margin-top:16px;width:22px}
.card p{font-size:11px;line-height:17.5px;color:var(--muted);margin-top:28px}

/* vision */
.vision{top:1326px;height:606px;color:var(--white)}
.vision-photo{position:absolute;inset:0;
  background:
    radial-gradient(ellipse 190px 120px at 600px 560px,#e0a52a 0%,#9b6a14 45%,rgba(60,40,10,0) 80%),
    radial-gradient(ellipse 420px 260px at 560px 170px,#3f8f7e 0%,#1f5a55 45%,rgba(20,50,52,0) 85%),
    linear-gradient(180deg,#0f2429 0%,#17383b 45%,#142a2e 70%,#0b1719 100%)}
.vision .heading{position:relative;color:var(--white);font-size:29px;margin-top:80px}
.pillars{position:absolute;top:142px;left:110px;width:980px;display:flex;justify-content:space-between}
.pillar{width:320px;text-align:center}
.pillar h3{font-family:"Montserrat",sans-serif;font-weight:700;font-size:17px;margin-top:26px}
.pillar p{font-size:14px;line-height:19px;margin-top:10px;color:#eef4f2}

/* problem */
.problem{top:1932px;height:499px;background:var(--white)}
.problem .heading{margin-top:80px}
.issues{position:absolute;top:160px;left:120px;width:960px;display:flex}
.issue{flex:1;text-align:center;padding:0 20px;border-left:1px solid #e2e2e2;height:283px}
.issue:first-child{border-left:none}
.issue-icon{display:block;margin:0 auto}
.issue h3{font-family:"Montserrat",sans-serif;font-weight:700;font-size:13px;margin-top:30px}
.issue h4{font-family:"Montserrat",sans-serif;font-weight:600;font-size:12px;margin-top:10px}
.issue p{font-size:11px;line-height:17.5px;color:var(--muted);margin-top:26px}

/* solution */
.solution{top:2431px;height:620px;background:var(--panel)}
.solution-art{position:absolute;left:132px;top:74px;width:525px;height:435px;
  background:
    radial-gradient(ellipse 200px 120px at 300px 330px,#3b4a5e 0%,rgba(59,74,94,0) 100%),
    radial-gradient(ellipse 160px 120px at 180px 200px,rgba(240,120,40,.55),rgba(240,120,40,0) 100%),
    radial-gradient(ellipse 140px 90px at 110px 260px,rgba(90,170,80,.55),rgba(90,170,80,0) 100%),
    radial-gradient(ellipse 260px 200px at 260px 220px,#c8d2dc 0%,rgba(200,210,220,0) 100%)}
.solution-copy{position:absolute;left:709px;top:68px;width:345px}
.solution-copy h2{font-family:"Montserrat",sans-serif;font-weight:700;font-size:19px}
.solution-copy p{font-size:14px;line-height:24px;color:#444;margin-top:30px}
.offer{display:flex;align-items:center;width:278px;height:80px;background:var(--white);margin-top:10px;padding-left:20px;box-shadow:0 1px 4px rgba(0,0,0,.08)}
.offer:first-of-type{margin-top:24px}
.offer svg{margin-right:26px;flex:none}
.offer b{display:block;font-family:"Montserrat",sans-serif;font-weight:700;font-size:13px}
.offer span{display:block;font-size:11px;color:#555;margin-top:4px}
.section-curve{position:absolute;left:0}

/* contact */
.contact{top:3048px;height:345px;background:var(--white)}
.contact .heading{margin-top:82px}
.locations{position:absolute;left:194px;top:132px}
.col-title{font-family:"Montserrat",sans-serif;font-weight:700;font-size:13px}
.info-row{display:flex;align-items:center;gap:15px;margin-top:20px;font-size:14px}
.info-row svg{flex:none}
.form{position:absolute;left:753px;top:132px;width:260px}
.field{width:260px;height:32px;background:#e6e4e4;margin-top:10px;font-family:Arial,sans-serif;font-size:11px;padding:10px 11px;color:#333}
.field:first-of-type{margin-top:16px}
.field.tall{height:56px}
.btn-submit{margin-top:10px;height:43px;background:linear-gradient(180deg,#fbab2e,#f47f1b);color:var(--white);font-family:Arial,sans-serif;font-weight:700;font-size:13px;display:flex;align-items:center;justify-content:center;gap:8px}

/* footer */
.footer{top:3393px;height:390px;background:radial-gradient(ellipse at 50% 40%,#1a4aa8,var(--navy-deep) 70%);color:var(--white);text-align:center}
.footer-brand{margin-top:215px;font-family:"Montserrat",sans-serif;font-weight:600;font-size:32px;letter-spacing:12px}
.footer-line{font-size:13px;margin-top:28px}
.footer-nav{font-size:11px;margin-top:16px}
.footer-nav span{margin:0 9px}
.copyright{font-size:11px;margin-top:26px}
</style>
</head>
<body>

<section class="section hero">
  <div class="hero-photo" role="img" aria-label="White electric car plugged into a charging station with blue light streaks"></div>
  <header class="site-header">
    <div class="brand">BREVOK</div>
    <nav class="nav">
      <a class="active" href="#">HOME</a><a href="#">THE PROBLEM</a><a href="#">THE SOLUTION</a><a href="#">CONTACT US</a>
    </nav>
  </header>
  <div class="hero-box">
    <h1>ENABLING FAST<br>AND INTEGRATED<br>EV CHARGING<br>NETWORKS</h1>
    <span class="btn-read">READ MORE</span>
  </div>
  <div class="dots"><span></span><span></span><span class="on"></span><span></span><span></span></div>
  <svg class="hero-curve" width="1200" height="75" viewBox="0 0 1200 75">
    <path d="M0 0 L600 62 L1200 0 L1200 75 L0 75Z" fill="#f7f7f7"/>
    <path d="M0 0 L600 62 L1200 0 L1200 12 L600 72 L0 12Z" fill="#f7941d"/>
  </svg>
</section>

<section class="section why">
  <h2 class="heading">WHY CHOOSE US<span class="heading-rule"></span></h2>
  <div class="cards">
    <article class="card">
      <svg class="card-shape" width="295" height="470" viewBox="0 0 295 470"><path d="M0 0H295V408L147 460L0 408Z" fill="#fff"/><path d="M9 10H286V402L147 450L9 402Z" fill="none" stroke="#fbb03b"/><path d="M0 408L147 452L295 408V420L147 468L0 420Z" fill="#f7941d"/></svg>
      <div class="card-body">
        <svg class="card-icon" width="70" height="70" viewBox="0 0 70 70"><circle cx="35" cy="35" r="27" fill="none" stroke="#f7941d" stroke-width="9" stroke-dasharray="7 5.1"/><circle cx="35" cy="35" r="24" fill="#f7941d"/><circle cx="35" cy="35" r="15" fill="#fff"/><path d="M35 46V30M35 38c-6 0-9-4-9-9 6 0 9 4 9 9zM35 36c5 0 8-4 8-9-5 0-8 4-8 9z" fill="#f7941d" stroke="#f7941d" stroke-width="1.5"/></svg>
        <h3>BEST OF BREED<br>ECOSYSTEM</h3><span class="heading-rule"></span><p>We plan, design, and deploy EV(1) charging Solutions as a Service by leveraging a best-in-class multi-vendor and partner network with expertise to deliver EV Hardware, Software and Services as Turn-Key and Agnostic solutions</p></div>
    </article>
    <article class="card">
      <svg class="card-shape" width="295" height="470" viewBox="0 0 295 470"><path d="M0 0H295V408L147 460L0 408Z" fill="#fff"/><path d="M9 10H286V402L147 450L9 402Z" fill="none" stroke="#fbb03b"/><path d="M0 408L147 452L295 408V420L147 468L0 420Z" fill="#f7941d"/></svg>
      <div class="card-body">
        <svg class="card-icon" width="70" height="70" viewBox="0 0 70 70" fill="none" stroke="#f7941d" stroke-width="2.5"><circle cx="35" cy="35" r="13" stroke-dasharray="3 3"/><circle cx="35" cy="35" r="5" fill="#f7941d"/><path d="M24 24L6 6M6 6h10M6 6v10M46 24L64 6M64 6H54M64 6v10M24 46L6 64M6 64h10M6 64V54M46 46l18 18M64 64H54M64 64V54"/><rect x="2" y="2" width="66" height="66" stroke-dasharray="6 5" stroke-width="1.5"/></svg>
        <h3>SCALABILITY WITH<br>LITTLE TO NO INVESTMENT</h3><span class="heading-rule"></span><p>We offer the ability to charge in minutes making for a scalable and nationwide application. The EV platform is delivered via consumption-based models allowing cities and enterprises to outsource the EV solution without prohibitive upfront investments</p></div>
    </article>
    <article class="card">
      <svg class="card-shape" width="295" height="470" viewBox="0 0 295 470"><path d="M0 0H295V408L147 460L0 408Z" fill="#fff"/><path d="M9 10H286V402L147 450L9 402Z" fill="none" stroke="#fbb03b"/><path d="M0 408L147 452L295 408V420L147 468L0 420Z" fill="#f7941d"/></svg>
      <div class="card-body">
        <svg class="card-icon" width="70" height="70" viewBox="0 0 70 70"><circle cx="35" cy="30" r="17" fill="#f7941d"/><rect x="27" y="45" width="16" height="6" rx="2" fill="#f7941d"/><rect x="28" y="53" width="14" height="5" rx="2" fill="#f7941d"/><rect x="31" y="60" width="8" height="4" rx="2" fill="#f7941d"/><path d="M35 40V30m-6-4 6 4 6-4" fill="none" stroke="#fff" stroke-width="2.5"/><path d="M35 4v5M12 12l4 4M58 12l-4 4M5 30h6M59 30h6" stroke="#f7941d" stroke-width="2.5"/></svg>
        <h3>SUSTAINABLE<br>INNOVATION</h3><span class="heading-rule"></span><p>We enable a new, smart and high-power EV charging solution and consumer lifestyle powered by AI(2) with sustainability in mind. We incorporate solar and other CO2 reducing technologies into our solution platform to augment power-limited grids when needed</p></div>
    </article>
  </div>
</section>

<section class="section vision">
  <div class="vision-photo" role="img" aria-label="Glowing tent under a night sky with green northern lights over mountains"></div>
  <h2 class="heading">Our Vision</h2>
  <div class="pillars">
    <div class="pillar">
      <svg width="120" height="104" viewBox="0 0 120 104"><path d="M60 2L118 102H2Z" fill="none" stroke="#fff" stroke-width="2"/><g fill="none" stroke="#f7941d" stroke-width="1.8"><circle cx="60" cy="70" r="15"/><ellipse cx="60" cy="70" rx="6" ry="15"/><path d="M45 70h30M48 62h24M48 78h24"/><path d="M40 52a4 4 0 1 1 8 0c0 3-4 7-4 7s-4-4-4-7zM72 52a4 4 0 1 1 8 0c0 3-4 7-4 7s-4-4-4-7z"/></g></svg>
      <h3>eV(1) anywhere &amp; everywhere</h3>
      <p>Enable access to EV charging stations on every city corner, interstate highways as well as rural and underserved areas</p>
    </div>
    <div class="pillar">
      <svg width="120" height="104" viewBox="0 0 120 104"><path d="M60 2L118 102H2Z" fill="none" stroke="#fff" stroke-width="2"/><g fill="none" stroke="#f7941d" stroke-width="1.8"><circle cx="52" cy="64" r="9" stroke-width="5" stroke-dasharray="3.5 2.6"/><circle cx="52" cy="64" r="4"/><circle cx="70" cy="80" r="8" stroke-width="5" stroke-dasharray="3.2 2.4"/><circle cx="70" cy="80" r="3.5"/><path d="M40 84a22 22 0 0 1-4-10M80 56a22 22 0 0 1 4 10"/></g></svg>
      <h3>FAST &amp; INTEGRATED SOLUTION</h3>
      <p>Provide high-power, open access EV charging networks and pay systems fueled by smart energy technologies</p>
    </div>
    <div class="pillar">
      <svg width="120" height="104" viewBox="0 0 120 104"><path d="M60 2L118 102H2Z" fill="none" stroke="#fff" stroke-width="2"/><g fill="none" stroke="#f7941d" stroke-width="1.8"><circle cx="60" cy="64" r="13"/><path d="M52 58c4 2 6 0 8 3s-2 6 2 8M64 53c0 4 4 4 6 8"/><path d="M38 72c4 6 10 12 22 14 12-2 18-8 22-14M38 72l4-4 6 8M82 72l-4-4-6 8"/></g></svg>
      <h3>Sustainability</h3>
      <p>Deploy citywide ESG(2) solutions that leverage green technology and help reduce carbon footprint, fossil fuel residue and harmful gas re-leased back into the environment</p>
    </div>
  </div>
</section>

<section class="section problem">
  <h2 class="heading">THE PROBLEM</h2>
  <div class="issues">
    <div class="issue">
      <svg class="issue-icon" width="78" height="78" viewBox="0 0 78 78"><defs><linearGradient id="og" x1="0" y1="0" x2="0" y2="1"><stop offset="0" stop-color="#fbb03b"/><stop offset="1" stop-color="#f26b1d"/></linearGradient></defs><circle cx="39" cy="39" r="39" fill="url(#og)"/><rect x="25" y="20" width="20" height="34" rx="2" fill="none" stroke="#fff" stroke-width="2.5"/><path d="M21 56h28" stroke="#fff" stroke-width="2.5"/><path d="M37 25l-6 10h6l-4 9 9-12h-6l4-7z" fill="#fff"/><path d="M45 32h5v14a3 3 0 0 0 6 0V30l-4-4" fill="none" stroke="#fff" stroke-width="2.5"/></svg>
      <h3>LIMITED</h3><h4>Charging Infrastructure</h4><p>Current EV charging network is 70 miles apart. Primarily planned in cities and interstate highways, excluding rural, small cities and underserved areas</p></div>
    <div class="issue">
      <svg class="issue-icon" width="78" height="78" viewBox="0 0 78 78"><circle cx="39" cy="39" r="39" fill="url(#og)"/><rect x="27" y="18" width="24" height="38" rx="3" fill="none" stroke="#fff" stroke-width="2.5"/><rect x="31" y="23" width="16" height="14" fill="none" stroke="#fff" stroke-width="2"/><path d="M37 30c0-3 3-4 5-4-1 3-2 5-5 4z" fill="#fff"/><rect x="31" y="42" width="10" height="8" fill="none" stroke="#fff" stroke-width="2"/><path d="M41 44h5M41 48h5" stroke="#fff" stroke-width="2"/></svg>
      <h3>SLOW</h3><h4>Charging Stations</h4><p>Most EV chargers deployed today are Levels I and II, which are very slow and impractical for city fleets. Current grid would cost billions to upgrade.</p></div>
    <div class="issue">
      <svg class="issue-icon" width="78" height="78" viewBox="0 0 78 78"><circle cx="39" cy="39" r="39" fill="url(#og)"/><circle cx="39" cy="27" r="10" fill="none" stroke="#fff" stroke-width="2.5"/><text x="39" y="32" text-anchor="middle" font-family="Montserrat,sans-serif" font-weight="700" font-size="13" fill="#fff">$</text><path d="M18 44l8 14h9l-6-12c-2-3-6-5-11-2zM60 44l-8 14h-9l6-12c2-3 6-5 11-2z" fill="none" stroke="#fff" stroke-width="2.5" stroke-linejoin="round"/></svg>
      <h3>LEGACY</h3><h4>Payment System</h4><p>Existing EV charging networks have multiple payment systems. Each vendor has its own proprietary app that caters only to their specific charging station.</p></div>
    <div class="issue">
      <svg class="issue-icon" width="78" height="78" viewBox="0 0 78 78"><g fill="url(#og)"><circle cx="39" cy="22" r="16"/><circle cx="24" cy="34" r="14"/><circle cx="54" cy="34" r="14"/><circle cx="39" cy="40" r="14"/><path d="M35 46h8v26h-8z"/><path d="M28 74h22v3H28z"/></g><path d="M39 52l-8-8M39 48l7-7" stroke="#fff" stroke-width="2.5"/></svg>
      <h3>SURGE</h3><h4>of Carbon Footprint</h4><p>The Green Earth Trust suggests that the average carbon footprint for a U.S. citizen is 16 tons. This is one of the highest rates in the world, leading to new policies implemented to reduce carbon footprint</p></div>
  </div>
</section>

<section class="section solution">
  <div class="solution-art" role="img" aria-label="Isometric illustration of EV charging stations, a street lamp and a car in a parking lot"></div>
  <div class="solution-copy">
    <h2>THE SOLUTION</h2>
    <p>End-to-End deployment and integration of EV charging Solution as a Service Cities and enterprises outsource the EV infrastructure, billing and on-going maintenance</p>
    <div class="offer"><svg width="44" height="44" viewBox="0 0 44 44" fill="none" stroke="#f7941d" stroke-width="2.2"><rect x="4" y="18" width="10" height="24"/><rect x="16" y="6" width="12" height="36"/><rect x="30" y="14" width="10" height="28"/><path d="M20 12h4M20 18h4M20 24h4M20 30h4M7 24h4M7 30h4M33 20h4M33 26h4M33 32h4M22 2v4"/></svg><div><b>PUBLIC SECTOR</b><span>Smart City Projects</span></div></div>
    <div class="offer"><svg width="44" height="44" viewBox="0 0 44 44" fill="none" stroke="#f7941d" stroke-width="2.2"><path d="M4 30l4-10h20l6 10v6H4z"/><circle cx="12" cy="36" r="3" fill="#f7941d"/><circle cx="28" cy="36" r="3" fill="#f7941d"/><rect x="30" y="6" width="10" height="12" rx="2"/><path d="M33 6V2M37 6V2M35 18v6"/></svg><div><b>HYBRID</b><span>Public Private Partnerships</span></div></div>
    <div class="offer"><svg width="44" height="44" viewBox="0 0 44 44" fill="none" stroke="#f7941d" stroke-width="2.2"><rect x="10" y="4" width="24" height="38"/><path d="M15 10h4M25 10h4M15 16h4M25 16h4M15 22h4M25 22h4M15 28h4M25 28h4M19 42v-7h6v7M4 42h36"/></svg><div><b>PRIVATE</b><span>Enterprise Businesses</span></div></div>
  </div>
  <svg class="section-curve" style="top:540px" width="1200" height="80" viewBox="0 0 1200 80">
    <path d="M0 0 L600 70 L1200 0 V80 H0Z" fill="#fff"/>
    <path d="M0 0 L600 68 L1200 0 V10 L600 78 L0 10Z" fill="#f7941d"/>
  </svg>
</section>

<section class="section contact">
  <h2 class="heading">CONTACT US</h2>
  <div class="locations">
    <div class="col-title">LOCATIONS</div>
    <div class="info-row"><svg width="24" height="24" viewBox="0 0 24 24"><circle cx="12" cy="12" r="12" fill="#1c1c3a"/><path d="M8 7l2-1 2 3-1 1c.5 1.5 1.5 2.5 3 3l1-1 3 2-1 2c-4 0-9-5-9-9z" fill="#fff"/></svg>954-XXX-XXXX</div>
    <div class="info-row"><svg width="24" height="24" viewBox="0 0 24 24"><circle cx="12" cy="12" r="12" fill="#1c1c3a"/><rect x="6.5" y="8" width="11" height="8" fill="#fff"/><path d="M6.5 8l5.5 4 5.5-4" fill="none" stroke="#1c1c3a"/></svg>info@brevok.com</div>
    <div class="info-row"><svg width="24" height="24" viewBox="0 0 24 24"><circle cx="12" cy="12" r="12" fill="#1c1c3a"/><path d="M12 5a4 4 0 0 1 4 4c0 3-4 9-4 9s-4-6-4-9a4 4 0 0 1 4-4z" fill="#fff"/><circle cx="12" cy="9" r="1.5" fill="#1c1c3a"/></svg><span>212 ,Lorem ipsum dolor<br>consectetur adipiscing</span></div>
    <div class="info-row"><svg width="24" height="24" viewBox="0 0 24 24"><circle cx="12" cy="12" r="12" fill="#1c1c3a"/><rect x="7" y="7" width="10" height="10" rx="1" fill="#fff"/><rect x="9" y="9" width="6" height="2" fill="#1c1c3a"/></svg>123-456-7890</div>
  </div>
  <div class="form">
    <div class="col-title">GET IN TOUCH</div>
    <div class="field">Enter Name:</div>
    <div class="field">Enter Email:</div>
    <div class="field tall">Message:</div>
    <div class="btn-submit">SUBMIT NOW <svg width="13" height="13" viewBox="0 0 13 13"><circle cx="6.5" cy="6.5" r="6.5" fill="#fff"/><path d="M4 6.5h5M7 4l2.5 2.5L7 9" fill="none" stroke="#f47f1b" stroke-width="1.5"/></svg></div>
  </div>
</section>

<section class="section footer">
  <svg class="section-curve" style="top:0" width="1200" height="80" viewBox="0 0 1200 80">
    <path d="M0 0 H1200 L600 70Z" fill="#fff"/>
    <path d="M0 0 L600 70 L1200 0 V10 L600 80 L0 10Z" fill="#f7941d"/>
  </svg>
  <div class="footer-brand">BREVOK</div>
  <p class="footer-line">Email: info@brevok.com &nbsp; | &nbsp; Phone: 954-XXX-XXXX</p>
  <p class="footer-nav">HOME<span>|</span>THE PROBLEM<span>|</span>THE SOLUTION<span>|</span>CONTACT US</p>
  <p class="copyright">Copyright © 2023 All Rights Reserved</p>
</section>

</body>
</html>
```